Website Design for Non-profit

We are looking for a new site design for the Patrons of the Northern Heritage Hall. The current site can be found at
http://www.patrons-hall.org/pnhhindex_e.html
The URL is provided for reference. We want a completely different look and layout which is shown in the specifications document. Visiting the site, you can learn more about the organization.
Initially, we would like a home page, and inside page provided. Once we a home page and inside page are selected, we would like a simple mobile template provided.
I have attached a full description of the project as well as the specifications document and a zip file containing images for the site.
As mentioned in the specs document, we want to include an image of the museum in the header. The zip file is too large for us to upload (80 meg). The zip file can be obtained by clicking this link:
http://qzl.cc/TrWpKe
The zip file contains several exterior photos and you can select the one you feel is most appropriate to your design.
Reason: A long weekend is coming up and a few members of the team are unavailable for review.
Reason: Reviewing designs. Should have a decision next week.
Reason: We are discussing the designs and looking to reach a consensus. I will be implementing some designs today or tomorrow. Hopefully final selection will be next week.
Reason: Still reviewing designs. Hope to get a decision soon.
Reason: Working to finalize the design. Very close.
Industry/Entity Type
Museum
Look and feel
Each slider illustrates characteristics of the customer's brand and the style your logo design should communicate.

```html
<!DOCTYPE html>
<html lang="en">
<head>
<meta charset="utf-8">
<title>Patrons of the Northern Heritage Hall</title>
<link href="https://fonts.googleapis.com/css2?family=Oswald:wght@300;400;500&family=Ubuntu:wght@400;500;700&display=swap" rel="stylesheet">
<style>
:root{
  --bg:#f5efe1;
  --blue:#2aa3d6;
  --tan:#a09673;
  --tan-dark:#8a8060;
  --panel:#e6dcc4;
  --ink:#3a3a3a;
  --muted:#8c8c8c;
  --rule:#d8cfb8;
}
*{margin:0;padding:0;box-sizing:border-box}
html,body{width:842px;height:1200px;overflow:hidden;background:var(--bg)}
body{position:relative;font-family:"Ubuntu",sans-serif;color:var(--ink)}
.abs{position:absolute}
.brand{left:14px;top:30px;display:flex;align-items:center;gap:12px}
.brand-mark{width:40px;height:40px;background:var(--blue)}
.brand-name{font-size:26px;font-weight:700;letter-spacing:10px;color:#222}
.account{left:648px;top:27px;font-size:13px;font-weight:700;color:var(--tan)}
.social{top:17px;width:23px;height:23px;background:var(--tan)}
.utility{left:535px;top:50px;font-size:10px;color:var(--muted);display:flex;gap:11px;letter-spacing:.2px}
.search{left:535px;top:67px;width:291px;height:26px;border-radius:13px;background:var(--tan);color:#fff;font-size:11px;padding:7px 14px}
.search svg{position:absolute;right:12px;top:5px}
.nav{left:9px;top:101px;width:824px;height:34px;background:var(--blue);display:flex;justify-content:space-between;align-items:center;padding:0 18px 0 21px}
.nav a{font-family:"Oswald",sans-serif;font-weight:300;font-size:17px;color:#fff;text-decoration:none;letter-spacing:-.3px}
.hero{left:0;top:135px;width:842px;height:276px;background:linear-gradient(90deg,#6f6f55 0%,#8b8a6a 35%,#6c6650 65%,#5a4f42 100%)}
.tabs{left:9px;top:426px;display:flex;font-family:"Oswald",sans-serif;font-weight:300;font-size:13px}
.tab{height:30px;padding:7px 12px;color:#333}
.tab.is-active{background:var(--tan);color:#fff}
.tab-panel{left:9px;top:456px;width:824px;height:122px;border:1px solid var(--tan)}
.tab-photo{position:absolute;left:9px;top:9px;width:138px;height:103px;background:linear-gradient(135deg,#c4ccd3,#8b8f92)}
.tab-text{position:absolute;left:159px;top:10px;width:652px;font-size:10.5px;line-height:12.5px;color:#555}
.tab-text p+p{margin-top:12px}
.side{left:9px;width:160px}
.side-btn{height:30px;background:var(--blue);color:#fff;font-size:12.5px;padding:7px 12px}
.side-note{background:var(--panel);padding:9px 10px;font-size:10px;line-height:12.5px;color:#555;height:96px}
.side-note .more{margin-top:14px}
.side-card{background:var(--tan);padding:8px 6px 6px}
.side-card h3{font-weight:400;font-size:12.5px;color:#fff;padding:0 6px 8px}
.side-card .ph{height:86px}
.post{left:215px;width:595px}
.post h2{font-family:"Oswald",sans-serif;font-weight:500;font-size:23px;color:var(--tan);letter-spacing:-.5px;line-height:28px}
.post .date{font-size:11px;color:#555;margin-top:4px}
.post-body{display:flex;gap:17px;margin-top:10px}
.post-img{flex:0 0 121px;height:89px}
.post-text{font-size:10.5px;line-height:12.5px;color:#444}
.post-text p+p{margin-top:12px}
.post-rule{left:215px;width:593px;height:1px;background:var(--rule)}
.play{position:absolute;left:27px;top:12px}
.foot-rule{left:9px;top:1126px;width:824px;height:1px;background:var(--tan)}
.foot-nav{left:13px;top:1137px;display:flex;gap:6px;font-size:9.5px;color:var(--tan)}
.foot-copy{left:13px;top:1155px;font-size:7.5px;line-height:10px;color:#666}
.partners{left:611px;top:1144px;display:flex;align-items:center;gap:12px;font-size:8px;color:var(--blue);line-height:9px}
.partners .torch{color:#a33;font-weight:700;font-size:9px}
.partners .sq{width:28px;height:28px;background:var(--blue)}
</style>
</head>
<body>
<header>
  <div class="abs brand"><span class="brand-mark"></span><span class="brand-name">PNHH</span></div>
  <div class="abs account">LOGIN &nbsp;|&nbsp; REGISTER</div>
  <span class="abs social" style="left:773px"></span>
  <span class="abs social" style="left:800px"></span>
  <div class="abs utility"><span>CONTACT</span><span>RELATED SITES</span><span>DONATE</span><span>SITEMAP</span><span>FRANCAIS</span></div>
  <div class="abs search">Search
    <svg width="18" height="16" viewBox="0 0 18 16"><circle cx="6.5" cy="6.5" r="5" fill="none" stroke="#fff" stroke-width="2"/><line x1="10" y1="10" x2="16" y2="15" stroke="#fff" stroke-width="2.5"/></svg>
  </div>
  <nav class="abs nav"><a>HOME</a><a>ABOUT</a><a>SUPPORT PNHH</a><a>EVENTS</a><a>PROJECTS &amp; PROGRAMS</a><a>MEET THE FRIENDS</a><a>VOLUNTEERS</a><a>PUBLICATIONS</a></nav>
</header>

<div class="abs hero" role="img" aria-label="Gallery hall with framed portraits and a group of schoolchildren visiting"></div>

<section>
  <div class="abs tabs"><span class="tab is-active">Be a Friend</span><span class="tab">Be a Donor</span><span class="tab">Be a Volunteer</span></div>
  <div class="abs tab-panel">
    <div class="tab-photo" role="img" aria-label="Two hands in a handshake against a cloudy sky"></div>
    <div class="tab-text">
      <p>Lorem ipsum dolor sit amet, consectetur adipisicing elit, sed do eiusmod tempor incididunt ut labore et dolore magna aliqua. Ut enim ad minim veniam, quis nostrud exercitation ullamco laboris nisi ut aliquip ex ea commodo consequat. Duis aute irure dolor in reprehenderit in voluptate velit esse cillum dolore eu fugiat nulla pariatur. Excepteur sint occaecat cupidatat non proident, sunt in culpa qui officia deserunt mollit anim id est laborum.</p>
      <p>Sed ut perspiciatis, unde omnis iste natus error sit voluptatem accusantium doloremque laudantium, totam rem aperiam eaque ipsa, quae ab illo inventore veritatis et quasi architecto beatae vitae dicta sunt, explicabo. Nemo enim ipsam voluptatem, quia voluptas sit,</p>
    </div>
  </div>
</section>

<aside>
  <div class="abs side side-btn" style="top:613px">Become a Volunteer</div>
  <div class="abs side side-btn" style="top:648px">Donate Now</div>
  <div class="abs side side-btn" style="top:682px">Speakers Bureau</div>
  <div class="abs side side-note" style="top:712px">Lorem ipsum dolor sit amet, consectetur adipisicing elit, sed do eiusmod tempor incididunt .<div class="more">read more +</div></div>
  <div class="abs side side-card" style="top:812px"><h3>Photo Gallery</h3><div class="ph" role="img" aria-label="Exhibition floor with a tank and artillery" style="background:linear-gradient(135deg,#5d6a6c,#3a3d38)"></div></div>
  <div class="abs side side-card" style="top:946px"><h3>Member Treasures</h3><div class="ph" role="img" aria-label="Row of service medals with striped ribbons" style="background:linear-gradient(90deg,#8a5b55,#c9b9a6,#7b4a46)"></div></div>
</aside>

<main>
  <article class="abs post" style="top:608px">
    <h2>Volunteers Visit the Vaults</h2>
    <div class="date">31 January, 2013</div>
    <div class="post-body">
      <div class="post-img" role="img" aria-label="Uniform jackets displayed in a storage vault" style="background:linear-gradient(135deg,#7d8466,#4f5444)"></div>
      <div class="post-text"><p>About thirty volunteers visited a couple of the NHH vaults at the invitation of Marion Tesk, the Hall’s Volunteer Coordinator. Divided into two groups and led by curators Paul Ardent and Lina Brovard , the tour included the Arms and Dress and Insignia vaults, both of which proved to be treasure trove of amazing, interesting artifacts.</p><p>The sections of the Arms vault visited contained a collection of helmets that included some donated by the Old Harbour Keep that dated back to the 16th Century.</p></div>
    </div>
  </article>
  <div class="abs post-rule" style="top:772px"></div>
  <article class="abs post" style="top:790px">
    <h2>2013 Welland Award Winners</h2>
    <div class="post-body">
      <div class="post-img" role="img" aria-label="Row of service medals with striped ribbons" style="background:linear-gradient(90deg,#8a5b55,#c9b9a6,#7b4a46)"></div>
      <div class="post-text"><p>The Patrons of the Northern Heritage Hall are pleased to announce the 2013 winners of the prestigious Colonel Arthur J. Welland History Award.  Five high school seniors from across Canada have received the award in recognition of their outstanding works of art and scholarship on the theme of Canada and the Korean War. Judged by a multi-disciplinary committee, the annual Colonel Arthur J. Welland History Awards are open to all graduating high school seniors and carry a $1000 cash prize</p></div>
    </div>
  </article>
  <article class="abs post" style="top:948px">
    <h2>Video Content about The Hall</h2>
    <div class="post-body">
      <div class="post-img" role="img" aria-label="Video still of visitors in a gallery" style="position:relative;background:linear-gradient(135deg,#b9a24a,#5d5a3c)">
        <svg class="play" width="66" height="66" viewBox="0 0 66 66"><circle cx="33" cy="33" r="30" fill="rgba(255,255,255,.25)" stroke="#fff" stroke-width="2.5"/><polygon points="26,19 26,47 48,33" fill="#fff"/></svg>
      </div>
      <div class="post-text"><p>About thirty volunteers visited a couple of the NHH vaults at the invitation of Marion Tesk, the Hall’s Volunteer Coordinator. Divided into two groups and led by curators Paul Ardent and Lina Brovard , the tour included the Arms and Dress and Insignia vaults, both of which proved to be treasure trove of amazing, interesting artifacts.</p><p>The sections of the Arms vault visited contained a collection of helmets that included some donated by the Old Harbour Keep that dated back to the 16th Century.</p></div>
    </div>
  </article>
</main>

<footer>
  <div class="abs foot-rule"></div>
  <div class="abs foot-nav"><span>HOME</span><span>ABOUT</span><span>SUPPORT PNHH</span><span>EVENTS</span><span>PROJECTS &amp; PROGRAMS</span><span>MEET THE FRIENDS</span><span>VOLUNTEERS</span><span>PUBLICATIONS</span></div>
  <div class="abs foot-copy">Copyright 2013 Patrons of the Northern Heritage Hall. All Rights Reserved.<br>12 Ridgeway Place, Northbrook, Ontario K0X 1A1</div>
  <div class="abs partners">
    <span class="torch">Passing<br>the Lamp</span>
    <span>NORTHERN<br>HERITAGE HALL</span>
    <span class="sq"></span>
    <span>SALLE DU<br>PATRIMOINE</span>
  </div>
</footer>
</body>
</html>
```